Garnett and Lyle Personal Injury Billboard

We'd like a clean/modern billboard to build brand awareness for our law firm in the area of personal injury. Ideally, we like the word "Injured?" or something similar in large lettering.

I'm attaching images, logo and award badges which could be used. The billboards will be 14x48 ft and 10.6x36.

We are open to different color ideas, fonts, and artwork. Creative but not too busy with wording. Our web page is www.kgarnettfirm.example

Garnett & Lyle Law Firm
(555) 318-4092

```html
<!DOCTYPE html>
<html lang="en">
<head>
<meta charset="utf-8">
<title>Garnett &amp; Lyle – Injured? Billboard</title>
<link rel="stylesheet" href="https://fonts.googleapis.com/css2?family=Montserrat:wght@400;500;600;700;800&display=swap">
<style>
  :root {
    --page-bg: #eef0f3;
    --board-bg: #0a0c11;
    --board-glow: #1c2a3d;
    --headline: #f4f8fc;
    --accent-light: #8fd0ef;
    --pill-blue: #1f5aa6;
    --band-blue: #1d4c88;
    --band-blue-dark: #163a6a;
    --badge-blue: #2a8fd8;
    --white: #ffffff;
    --photo-top: #3a3d44;
    --photo-bottom: #6d6a68;
  }
  * { margin: 0; padding: 0; box-sizing: border-box; }
  html, body {
    width: 710px; height: 1200px; overflow: hidden;
    background: var(--page-bg);
    font-family: "Montserrat", sans-serif;
  }
  .canvas {
    position: relative; width: 710px; height: 1200px;
    display: flex; align-items: center; justify-content: center;
  }
  .billboard {
    position: relative; width: 710px; height: 207px; overflow: hidden;
    background: radial-gradient(ellipse at 10% 10%, var(--board-glow) 0%, var(--board-bg) 45%);
    box-shadow: 0 2px 4px rgba(0,0,0,.35);
  }
  .firm-name {
    position: absolute; left: 28px; top: 20px;
    color: var(--white); font-weight: 700; font-size: 15px;
    line-height: 1.05; letter-spacing: .5px; text-transform: uppercase;
    white-space: nowrap;
  }
  .firm-name span { display: block; }
  .firm-name small {
    display: block; margin-top: 3px;
    font-size: 7px; font-weight: 600; letter-spacing: 1.6px;
    text-transform: none;
  }
  .attorney-photos {
    position: absolute; left: 0; top: 74px; width: 250px; height: 133px;
    background: linear-gradient(180deg, var(--photo-top) 0%, var(--photo-bottom) 100%);
  }
  .web-band {
    position: absolute; left: 243px; top: 182px; width: 467px; height: 25px;
    background: linear-gradient(90deg, var(--band-blue-dark), var(--band-blue));
    clip-path: polygon(0 0, 100% 0, 100% 100%, 8px 100%);
    display: flex; align-items: center; justify-content: center;
    color: var(--white); font-size: 15px; font-weight: 400; letter-spacing: .3px;
    white-space: nowrap;
  }
  .web-band strong { font-weight: 700; }
  .headline {
    position: absolute; left: 222px; top: 16px; width: 412px;
    text-align: center; color: var(--headline);
    font-weight: 700; font-size: 78px; line-height: 1; letter-spacing: -1px;
    white-space: nowrap;
  }
  .call-line {
    position: absolute; left: 222px; top: 102px; width: 412px;
    text-align: center; font-size: 30px; line-height: 1; white-space: nowrap;
  }
  .call-line .call-label { color: var(--accent-light); font-weight: 500; }
  .call-line .phone { color: var(--white); font-weight: 700; }
  .practice-areas {
    position: absolute; left: 238px; top: 148px;
    display: flex; gap: 8px; list-style: none;
  }
  .practice-areas li {
    height: 18px; border-radius: 9px;
    background: var(--pill-blue); color: var(--white);
    font-size: 9.5px; font-weight: 600; letter-spacing: .8px;
    white-space: nowrap;
    display: flex; align-items: center; justify-content: center;
  }
  .practice-areas .auto { width: 108px; }
  .practice-areas .medical { width: 144px; }
  .practice-areas .work { width: 108px; }
  .award-badge {
    position: absolute; left: 645px; top: 107px; width: 46px; height: 64px;
  }
</style>
</head>
<body>
<main class="canvas">
  <section class="billboard" aria-label="Garnett &amp; Lyle personal injury billboard">
    <div class="firm-name"><span>Garnett</span><span>&amp; Lyle</span><small>Law Firm PLLC</small></div>

    <div class="attorney-photos" role="img" aria-label="Portrait photo of the two firm attorneys in suits"></div>

    <h1 class="headline">INJURED?</h1>

    <p class="call-line"><span class="call-label">CALL US</span> <span class="phone">(555) 318-4092</span></p>

    <ul class="practice-areas">
      <li class="auto">AUTO ACCIDENT</li>
      <li class="medical">MEDICAL MALPRACTICE</li>
      <li class="work">WORK INJURY</li>
    </ul>

    <svg class="award-badge" viewBox="0 0 46 64" role="img" aria-label="Community award badge">
      <rect x="1" y="1" width="44" height="62" fill="var(--badge-blue)" stroke="var(--white)" stroke-width="2"/>
    </svg>

    <div class="web-band">www.<strong>kgarnettfirm</strong>.example</div>
  </section>
</main>
</body>
</html>
```